Innovative Beverage Company needs a Packaging Design/Line Extension

We need a packaging design for a line extension for a new flavour of our beverage line called Vexa. Vexa is a 7% alcohol by volume "cooler" sold in aluminium cans. Its packaging is known for is bright colours and graphic design.

We are looking for a design that will "fit" with our existing product line. To "fit" the design will need to be somewhat different to the current products, but also complimentary in terms of design and chosen colours.

Attached are the current designs that we use, and the die-line.

Target Market(s)

The target demographic are women from 18 to 30.

Industry/Entity Type

It Company

Requirements
Must have
• We are looking for a design that will "fit" with our existing product line. To "fit" the design will need to be somewhat different to the current products, but also complimentary in terms of design and chosen colours.

```html
<!DOCTYPE html>
<html lang="fr">
<head>
<meta charset="utf-8">
<title>Vexa – étiquette de canette</title>
<link rel="stylesheet" href="https://fonts.googleapis.com/css2?family=Quicksand:wght@400;500;700&display=swap">
<style>
  :root {
    --bg: #ececec;
    --label-white: #f4f4f2;
    --pink: #f4a6c8;
    --pink-deep: #ec86b3;
    --pink-soft: #f8c6dc;
    --lilac: #b9a2d8;
    --lime: #cfe59a;
    --butter: #f3e48c;
    --ink: #1d1d1d;
    --panel-text: #ffffff;
  }
  * { box-sizing: border-box; margin: 0; padding: 0; }
  html, body { width: 1200px; height: 1000px; overflow: hidden; }
  body {
    background: var(--bg);
    font-family: "Quicksand", sans-serif;
    color: var(--ink);
  }
  .can-label {
    position: absolute;
    left: 120px;
    top: 200px;
    width: 960px;
    height: 600px;
    display: flex;
    background: var(--label-white);
    box-shadow: 0 10px 30px rgba(0,0,0,0.08);
  }
  .side-panel {
    width: 230px;
    background: linear-gradient(90deg, var(--pink-deep), var(--pink));
    color: var(--panel-text);
    padding: 34px 22px;
    display: flex;
    flex-direction: column;
    gap: 14px;
    font-size: 12px;
    line-height: 1.45;
  }
  .side-panel .heading {
    background: var(--pink-soft);
    color: #ffffff;
    font-weight: 700;
    font-size: 13px;
    letter-spacing: 0.04em;
    padding: 4px 8px;
  }
  .side-panel .web { font-weight: 700; font-size: 13px; }
  .side-panel .legal { font-size: 10px; text-transform: uppercase; opacity: 0.95; margin-top: auto; }
  .main-panel {
    position: relative;
    flex: 1;
  }
  .pattern {
    position: absolute;
    inset: 0;
    background:
      linear-gradient(90deg,
        transparent 0 8%, rgba(244,166,200,0.55) 8% 12%, transparent 12% 22%,
        rgba(185,162,216,0.45) 22% 24%, transparent 24% 36%,
        rgba(207,229,154,0.5) 36% 39%, transparent 39% 52%,
        rgba(236,134,179,0.55) 52% 56%, transparent 56% 68%,
        rgba(243,228,140,0.5) 68% 71%, transparent 71% 84%,
        rgba(185,162,216,0.45) 84% 86%, transparent 86%),
      linear-gradient(180deg, rgba(248,198,220,0.35), rgba(244,244,242,0) 45%, rgba(248,198,220,0.35));
  }
  .brand {
    position: absolute;
    left: 250px;
    top: 250px;
    font-size: 96px;
    font-weight: 500;
    color: var(--ink);
    letter-spacing: 0.02em;
  }
  .abv {
    position: absolute;
    left: 262px;
    top: 375px;
    font-size: 28px;
    font-weight: 400;
  }
  .category {
    position: absolute;
    left: 40px;
    bottom: 22px;
    font-size: 20px;
    font-weight: 700;
    letter-spacing: 0.01em;
  }
</style>
</head>
<body>
  <div class="can-label">
    <aside class="side-panel">
      <p class="heading">SERVIR FROID</p>
      <p>Savourez la fraîcheur du fruit par une journée ensoleillée, le melon vous rafraîchit dès la première gorgée!</p>
      <p class="heading">SERVE CHILLED</p>
      <p>Discover the ultimate melon refreshment. You'll love this refreshing taste to the last drop.</p>
      <p class="web">drinkvexa.ca</p>
      <p class="legal">Cocktail de cidre pétillant et gazéifié. Sparkling cider cocktail. Consigné là où prescrit par la loi. Refund where applicable.</p>
    </aside>
    <section class="main-panel">
      <div class="pattern" role="img" aria-label="Motif décoratif de lignes verticales et spirales roses, lilas, lime et jaune"></div>
      <p class="brand">Vexa</p>
      <p class="abv">7 % alc./vol.</p>
      <p class="category">BOISSON ALCOOLISÉE ALTERNATIVE</p>
    </section>
  </div>
</body>
</html>
```